■書籍タイトル
「町工房・路地の店・士業のための、明日効く集客設計術・KRT」

・堅苦しくなく、わかりやすいイメージにしたいです
・電子書籍なので、画像が小さいので、できるだけ視認しやすい文字でお願いします

■オビ
「お金も時間もかけずに、たった2つのことをするだけで、ライバルが歯ぎしりするほどお客に選ばれる」

■著者  森野沙知絵
■発行  東陽商務文化出版舎

■色の指定などはありません。お任せです。
(明るい・カンタン・わかりやすい)
イメージイラストなど入ってもよいかと思います。

■高級感やアカデミックより、明るくカンタンなイメージで。

※参考資料として、書籍の原稿と、同じタイトルのセミナーのパワポ表紙画像を添付します。
アカデミックな感じより、ポップな感じや明るいイメージ、
「わかりやすさ」「文字の視認性」を重視します。
クラフターのみなさま、
引き続き、ご提案をお待ちしております。
みなさま、ご提案ありがとうございます。

中小企業・小さなお店・先生業
という文字が小さい表示のデザインが多いのですが、

ターゲット層が一目で見てわかるよう、

中小企業・小さなお店・先生業

という文字が見えるようにしたいです。

引き続き、みなさまからのご提案をお待ちしております。
たくさんのご提案をいただきありがとうございます。

本のタイトルが、変更となりました。
金額をアップし、締め切りを1日延長いたしますので、
訂正ご対応いただければ幸いです。

新しいタイトルは、

「中小企業・小さなお店・先生業が
常連が増え続けるために明日から始める三つの習慣」
です。

帯、またはサブタイトルは、
「ライバルが歯ぎしりするほどお客が押し寄せる新時代の差別化戦略」
としてください。

ご提案をお待ちしております。
よろしくお願いいたします。

今回の装丁は、特に「わかりやすさ」を重視しておりました。
レベルの高い装丁デザインが多く、選考に大変迷いました。
選定させていただきましたデザインは、笑顔の3職種の人物のイラストと、フォントの使い方など、わかりやすい・明るい・カンタンという目指すところをこちらの想定以上に表現していただいたことが一番の理由です。

たくさんのご提案をいただき、ありがとうございました。
本当にレベルの高いデザインが多く選定では社内でも意見が割れました。
また、再三の追記・変更によりお手数をおかけしましたことを、この場を借りてお詫び申し上げます。

今後も定期的に装丁の依頼をいたしますので、どうぞよろしくお願いいたします。

```html
<!DOCTYPE html>
<html lang="ja">
<head>
<meta charset="UTF-8">
<title>明日効く集客設計術・KRT</title>
<link rel="stylesheet" href="https://fonts.googleapis.com/css2?family=Noto+Sans+JP:wght@700;900&display=swap">
<style>
  :root {
    --cover-orange: #f5a31f;
    --ink: #1a1a1a;
    --paper: #ffffff;
    --street-tint: #fbe3b4;
  }
  html, body {
    margin: 0;
    padding: 0;
    overflow: hidden;
    background: var(--paper);
  }
  .cover {
    position: relative;
    width: 844px;
    height: 1200px;
    overflow: hidden;
    background: var(--cover-orange);
    font-family: "Noto Sans JP", sans-serif;
    color: var(--ink);
  }
  .street-illustration {
    position: absolute;
    left: 0;
    top: 0;
    width: 844px;
    height: 135px;
    background: linear-gradient(180deg, var(--cover-orange) 0%, var(--street-tint) 55%, var(--paper) 100%);
  }
  .speech-bubble {
    position: absolute;
    left: 30px;
    top: 130px;
    width: 420px;
    height: 660px;
  }
  .audience {
    position: absolute;
    top: 160px;
    right: 448px;
    margin: 0;
    writing-mode: vertical-rl;
    font-weight: 900;
    font-size: 74px;
    line-height: 1.05;
    letter-spacing: 0.02em;
  }
  .audience span { display: block; }
  .audience .line-3 { padding-top: 40px; }
  .band-copy {
    position: absolute;
    left: 430px;
    top: 170px;
    margin: 0;
    color: var(--paper);
    font-weight: 700;
    font-size: 39px;
    line-height: 1.36;
  }
  .title {
    position: absolute;
    right: 40px;
    top: 750px;
    margin: 0;
    text-align: right;
    font-weight: 900;
    font-size: 96px;
    line-height: 1.06;
    letter-spacing: 0.01em;
  }
  .title span { display: block; }
  .title .series {
    margin-right: 190px;
    font-size: 110px;
    letter-spacing: 0.04em;
  }
  .author {
    position: absolute;
    left: 40px;
    top: 1058px;
    margin: 0;
    font-weight: 900;
    font-size: 40px;
  }
  .author small { font-size: 30px; }
  .publisher {
    position: absolute;
    left: 40px;
    top: 1118px;
    margin: 0;
    font-weight: 700;
    font-size: 26px;
  }
</style>
</head>
<body>
  <main class="cover">
    <div class="street-illustration" role="img" aria-label="白い線で描かれた商店と事務所が並ぶ街並みのイラスト"></div>

    <svg class="speech-bubble" viewBox="0 0 420 660" aria-hidden="true">
      <path d="M210 10 C330 10 400 120 400 300 C400 420 380 500 330 560 L400 640 L280 600 C250 625 230 650 210 650 C90 650 20 520 20 330 C20 130 90 10 210 10 Z" fill="#ffffff"/>
    </svg>

    <h2 class="audience">
      <span class="line-1">町工房・</span>
      <span class="line-2">路地の店・</span>
      <span class="line-3">士業のための、</span>
    </h2>

    <p class="band-copy">
      お金も時間も<br>
      かけずに、<br>
      たった2つのことを<br>
      するだけで、<br>
      ライバルが<br>
      歯ぎしりするほど<br>
      お客に選ばれる！
    </p>

    <h1 class="title">
      <span>明日効く</span>
      <span>集客設計術・</span>
      <span class="series">KRT</span>
    </h1>

    <p class="author">森野沙知絵<small>著</small></p>
    <p class="publisher">東陽商務文化出版舎</p>
  </main>
</body>
</html>
```